Business Card Design Project

Want a modern business card.
Concern is that our email address is long and thus poses a design challenge.
Items like the company name can be omitted from text as it will be available via the logo.

Example:
Desmond Farraway
President / CEO
Cell 555.304.2817
Office 555.619.0352
desmondf@qtvnetworkplatforms.example
www.qtvnetworkplatforms.example

Target Market(s)

Technical and executive level members of Information Technology companies in the Healthcare industry.

Industry/Entity Type

Business

Colors

Designer to choose colors to be used in the design.

Requirements
Nice to have
• Raised logo, but I am open.

```html
<!DOCTYPE html>
<html lang="en">
<head>
<meta charset="UTF-8">
<title>QTV Network Platforms – Business Card</title>
<link rel="stylesheet" href="https://fonts.googleapis.com/css2?family=Cinzel:wght@700&family=Questrial&display=swap">
<style>
  :root {
    --bg: #cdfadb;
    --card-white: #ffffff;
    --card-blue: #0a2aa8;
    --card-blue-dark: #061d86;
    --brand-blue: #0b2c9c;
    --emboss-blue: #1a3cbc;
    --accent-red: #e0141e;
    --text-grey: #4a4f57;
    --icon-blue: #173a9e;
  }
  * { margin: 0; padding: 0; box-sizing: border-box; }
  html, body {
    width: 1200px;
    height: 856px;
    overflow: hidden;
    background: var(--bg);
  }
  .canvas {
    position: relative;
    width: 1200px;
    height: 856px;
  }
  .card {
    position: absolute;
    width: 520px;
    height: 300px;
    border-radius: 30px;
    box-shadow: 0 10px 28px rgba(40, 90, 60, 0.18);
  }
  .card-front {
    left: 60px;
    top: 300px;
    background: var(--card-white);
  }
  .card-back {
    left: 620px;
    top: 250px;
    background: linear-gradient(160deg, var(--card-blue) 0%, var(--card-blue-dark) 100%);
  }
  .brand {
    position: absolute;
    font-family: "Questrial", sans-serif;
    font-weight: 400;
    color: var(--brand-blue);
    line-height: 1;
    white-space: nowrap;
  }
  .card-front .brand {
    left: 54px;
    top: 62px;
    font-size: 28px;
  }
  .card-back .brand {
    left: 50%;
    top: 50%;
    transform: translate(-50%, -50%);
    font-size: 28px;
    color: var(--emboss-blue);
  }
  .identity {
    position: absolute;
    left: 222px;
    top: 116px;
  }
  .person-name {
    font-family: "Cinzel", serif;
    font-weight: 700;
    font-size: 14px;
    color: var(--accent-red);
    letter-spacing: 0.3px;
  }
  .person-title {
    font-family: "Questrial", sans-serif;
    font-size: 11px;
    color: var(--text-grey);
    margin-top: 2px;
  }
  .contact {
    position: absolute;
    left: 222px;
    top: 176px;
    list-style: none;
    font-family: "Questrial", sans-serif;
    font-size: 12.5px;
    color: var(--text-grey);
    line-height: 19px;
  }
  .contact li { display: flex; align-items: center; gap: 6px; white-space: nowrap; }
  .contact .icon { width: 12px; height: 12px; flex: none; }
</style>
</head>
<body>
<main class="canvas">
  <section class="card card-front" aria-label="Business card front">
    <div class="brand">QTV Network Platforms</div>
    <div class="identity">
      <p class="person-name">DESMOND FARRAWAY</p>
      <p class="person-title">President / CEO</p>
    </div>
    <ul class="contact">
      <li>Cell 555.304.2817</li>
      <li>Office 555.619.0352</li>
      <li>
        <svg class="icon" viewBox="0 0 12 12" aria-hidden="true">
          <rect width="12" height="12" rx="2" fill="var(--icon-blue)"/>
          <rect x="2.5" y="3.5" width="7" height="5" fill="none" stroke="#fff" stroke-width="0.9"/>
          <path d="M2.5 3.5 L6 6.5 L9.5 3.5" fill="none" stroke="#fff" stroke-width="0.9"/>
        </svg>
        desmondf@qtvnetworkplatforms.example
      </li>
      <li>
        <svg class="icon" viewBox="0 0 12 12" aria-hidden="true">
          <rect width="12" height="12" rx="2" fill="var(--icon-blue)"/>
          <circle cx="6" cy="6" r="3.4" fill="none" stroke="#fff" stroke-width="0.9"/>
          <ellipse cx="6" cy="6" rx="1.5" ry="3.4" fill="none" stroke="#fff" stroke-width="0.8"/>
          <line x1="2.6" y1="6" x2="9.4" y2="6" stroke="#fff" stroke-width="0.8"/>
        </svg>
        www.qtvnetworkplatforms.example
      </li>
    </ul>
  </section>

  <section class="card card-back" aria-label="Business card back">
    <div class="brand">QTV Network Platforms</div>
  </section>
</main>
</body>
</html>
```